Need a new design for Glass Cleaner label. The brand name already exists i.e. BRIXO. Pell is the company name. Looking for new design. It's application is for cleaning glasses in houses, cars, offices e.t.c. Our product gives streak free shine and anti static effect. Images of old label design is attached. Bottle will be same as before. It's better to show a car as well in the design but not necessary. New logo's of brixo can also be designed.

Target Market(s)

Household and automobile

Industry/Entity Type

It Company

```html
<!DOCTYPE html>
<html lang="en">
<head>
<meta charset="utf-8">
<title>Brixo Glass Cleaner Label</title>
<link rel="stylesheet" href="https://fonts.googleapis.com/css2?family=Sniglet:wght@800&family=Righteous&display=swap">
<style>
  :root {
    --cream: #f1e8b8;
    --sand: #d9c58c;
    --gold: #b79a55;
    --bronze: #8a6a2c;
    --ink: #231f20;
    --white: #ffffff;
  }
  html, body {
    margin: 0;
    padding: 0;
    width: 1200px;
    height: 423px;
    overflow: hidden;
    background: var(--cream);
  }
  .label {
    position: relative;
    width: 1200px;
    height: 423px;
    overflow: hidden;
  }
  .label__backdrop {
    position: absolute;
    inset: 0;
    background:
      radial-gradient(ellipse 70% 60% at 85% 40%, var(--cream) 0%, rgba(241,232,184,0) 70%),
      linear-gradient(100deg, var(--bronze) 0%, var(--gold) 18%, var(--sand) 45%, var(--cream) 80%);
  }
  .label__sweep {
    position: absolute;
    inset: 0;
  }
  .label__company {
    position: absolute;
    left: 10px;
    top: 20px;
    margin: 0;
    font-family: "Righteous", sans-serif;
    font-size: 34px;
    letter-spacing: 3px;
    line-height: 1;
    color: var(--ink);
  }
  .label__brand {
    position: absolute;
    left: 196px;
    top: 40px;
    margin: 0;
    font-family: "Sniglet", sans-serif;
    font-weight: 800;
    font-size: 272px;
    line-height: 1;
    letter-spacing: -4px;
    color: var(--ink);
  }
  .label__tagline {
    position: absolute;
    right: 12px;
    bottom: 14px;
    margin: 0;
    font-family: "Righteous", sans-serif;
    font-size: 40px;
    letter-spacing: 4px;
    line-height: 1;
    color: var(--ink);
    -webkit-text-stroke: 5px var(--cream);
    paint-order: stroke fill;
  }
</style>
</head>
<body>
  <main class="label">
    <div class="label__backdrop" role="img" aria-label="Gold and cream light streaks sweeping across the label with sparkling droplets"></div>
    <svg class="label__sweep" viewBox="0 0 1200 423" width="1200" height="423" aria-hidden="true">
      <path d="M0 300 C 250 300, 500 360, 720 423 L 0 423 Z" fill="var(--bronze)" opacity="0.75"/>
      <path d="M0 298 C 250 298, 500 358, 722 423" fill="none" stroke="var(--white)" stroke-width="3"/>
      <path d="M0 200 C 120 120, 260 40, 420 0" fill="none" stroke="var(--white)" stroke-width="2" opacity="0.8"/>
    </svg>
    <p class="label__company">PELL</p>
    <h1 class="label__brand">Brixo</h1>
    <p class="label__tagline">STREAK-FREE SHINE</p>
  </main>
</body>
</html>
```